TRU PEAK POWER.

I'd like my business logo.
contact name: Desmond Halvik
phone:0438275160
email: info@trupeakpower.net.au
website: www.trupeakpower.net.au

services:
solar
battery storage
LED lighting
energy saving solutions
general electrical
I'd like the design to look professional

Target Market(s)

Everyone

Industry/Entity Type

Business

Contact Information for Business Card

as described above

Requirements
Must have
• Id like the colours and the design to work well with my logo.

```html
<!DOCTYPE html>
<html lang="en">
<head>
<meta charset="utf-8">
<title>Tru Peak Power – Business Cards</title>
<link rel="stylesheet" href="https://fonts.googleapis.com/css2?family=Cabin:wght@500;700&display=swap">
<style>
  :root {
    --backdrop: #e3e3e3;
    --card-white: #ffffff;
    --green-light: #7cb843;
    --green-dark: #5e9a2e;
    --green-ink: #2f6a2a;
    --orange-light: #f9ab3c;
    --orange-dark: #f08a1e;
    --orange-ink: #a8501a;
    --brand-green: #3aa65a;
    --sun-orange: #f7a21b;
    --service-white: #ffffff;
  }
  * { margin: 0; padding: 0; box-sizing: border-box; }
  html, body {
    width: 1200px; height: 900px; overflow: hidden;
    background: var(--backdrop);
    font-family: "Cabin", "Gill Sans", sans-serif;
  }
  .card {
    position: absolute;
    width: 620px; height: 376px;
    background: var(--card-white);
    box-shadow: 0 6px 14px rgba(0,0,0,0.22);
    overflow: hidden;
  }
  .card--green { left: 40px; top: 60px; --band-light: var(--green-light); --band-dark: var(--green-dark); --ink: var(--green-ink); }
  .card--orange { left: 540px; top: 480px; --band-light: var(--orange-light); --band-dark: var(--orange-dark); --ink: var(--orange-ink); }

  .card__wave { position: absolute; inset: 0; width: 100%; height: 100%; }
  .wave-edge { fill: var(--band-dark); }
  .wave-fill { fill: var(--band-light); }

  .brand {
    position: absolute; left: 44px; top: 62px;
    display: flex; align-items: center; gap: 22px;
  }
  .brand__dot {
    width: 96px; height: 96px; border-radius: 50%;
    background: var(--sun-orange);
  }
  .brand__name {
    font-weight: 700; font-size: 54px; line-height: 1;
    color: var(--brand-green); letter-spacing: 1px;
  }

  .services {
    position: absolute; right: 26px; top: 150px;
    list-style: none; text-align: right;
    color: var(--service-white);
    font-weight: 700; font-size: 21px; line-height: 1.05;
    text-transform: uppercase;
  }

  .contact {
    position: absolute; left: 26px; bottom: 18px;
    color: var(--ink);
  }
  .contact__name { font-weight: 700; font-size: 22px; margin-bottom: 4px; padding-left: 8px; }
  .contact__list { list-style: none; font-weight: 500; font-size: 17px; line-height: 1.2; }
  .contact__list li { display: flex; align-items: center; gap: 6px; }
  .contact__icon { width: 14px; height: 14px; fill: none; stroke: var(--card-white); stroke-width: 1.6; flex: none; }
</style>
</head>
<body>

<article class="card card--green">
  <svg class="card__wave" viewBox="0 0 620 376" preserveAspectRatio="none" aria-hidden="true">
    <path class="wave-edge" d="M0,258 C150,214 260,250 390,184 C490,132 560,62 620,40 L620,376 L0,376 Z"/>
    <path class="wave-fill" d="M0,272 C150,230 270,264 400,198 C500,146 566,82 620,62 L620,376 L0,376 Z"/>
  </svg>
  <div class="brand">
    <span class="brand__dot"></span>
    <span class="brand__name">TRU PEAK POWER</span>
  </div>
  <ul class="services">
    <li>Solar</li><li>Battery Storage</li><li>LED Lighting</li><li>Energy Saving Solutions</li>
  </ul>
  <div class="contact">
    <p class="contact__name">Desmond Halvik</p>
    <ul class="contact__list">
      <li><svg class="contact__icon" viewBox="0 0 14 14"><path d="M3 1 L5 4 L4 6 C5 8 6 9 8 10 L10 9 L13 11 L11 13 C6 12 2 8 1 3 Z"/></svg>0438275160</li>
      <li><svg class="contact__icon" viewBox="0 0 14 14"><rect x="1" y="3" width="12" height="8"/><path d="M1 3 L7 8 L13 3"/></svg>info@trupeakpower.net.au</li>
      <li><svg class="contact__icon" viewBox="0 0 14 14"><circle cx="7" cy="7" r="6"/><path d="M1 7 H13 M7 1 C4 4 4 10 7 13 M7 1 C10 4 10 10 7 13"/></svg>www.trupeakpower.net.au</li>
    </ul>
  </div>
</article>

<article class="card card--orange">
  <svg class="card__wave" viewBox="0 0 620 376" preserveAspectRatio="none" aria-hidden="true">
    <path class="wave-edge" d="M0,258 C150,214 260,250 390,184 C490,132 560,62 620,40 L620,376 L0,376 Z"/>
    <path class="wave-fill" d="M0,272 C150,230 270,264 400,198 C500,146 566,82 620,62 L620,376 L0,376 Z"/>
  </svg>
  <div class="brand">
    <span class="brand__dot"></span>
    <span class="brand__name">TRU PEAK POWER</span>
  </div>
  <ul class="services">
    <li>Solar</li><li>Battery Storage</li><li>LED Lighting</li><li>Energy Saving Solutions</li>
  </ul>
  <div class="contact">
    <p class="contact__name">Desmond Halvik</p>
    <ul class="contact__list">
      <li><svg class="contact__icon" viewBox="0 0 14 14"><path d="M3 1 L5 4 L4 6 C5 8 6 9 8 10 L10 9 L13 11 L11 13 C6 12 2 8 1 3 Z"/></svg>0438275160</li>
      <li><svg class="contact__icon" viewBox="0 0 14 14"><rect x="1" y="3" width="12" height="8"/><path d="M1 3 L7 8 L13 3"/></svg>info@trupeakpower.net.au</li>
      <li><svg class="contact__icon" viewBox="0 0 14 14"><circle cx="7" cy="7" r="6"/><path d="M1 7 H13 M7 1 C4 4 4 10 7 13 M7 1 C10 4 10 10 7 13"/></svg>www.trupeakpower.net.au</li>
    </ul>
  </div>
</article>

</body>
</html>
```